MSA Plans

I would like to rebuild my brochure for the 3 business plans that I currently offer my clients. I would like to make it look much more modern & attractive to clients when choosing one of our service plans. If we can stick to a tech theme that would be great. Message me for anymore information.

```html
<!DOCTYPE html>
<html lang="en">
<head>
<meta charset="utf-8">
<title>MSA Plans – Service Plan Comparison</title>
<link href="https://fonts.googleapis.com/css2?family=Outfit:wght@300;400;600;700&display=swap" rel="stylesheet">
<style>
  :root{
    --bg-deep:#081440;
    --bg-mid:#112a78;
    --panel:#141b30;
    --orange:#ff3d00;
    --line:#4a2a30;
    --line-light:rgba(255,255,255,.35);
    --white:#ffffff;
    --tick:#3fe014;
    --cross:#ff1616;
  }
  *{box-sizing:border-box;margin:0;padding:0}
  html,body{width:928px;height:1200px;overflow:hidden}
  body{
    font-family:"Outfit",sans-serif;
    color:var(--white);
    background:radial-gradient(ellipse at 85% 20%,var(--bg-mid) 0%,var(--bg-deep) 55%),var(--bg-deep);
    position:relative;
  }
  .network-backdrop{position:absolute;inset:0;
    background:radial-gradient(circle at 10% 75%,rgba(40,90,220,.35),transparent 40%),
               radial-gradient(circle at 95% 45%,rgba(40,90,220,.3),transparent 35%);}
  .plan-panel{
    position:absolute;left:22px;width:884px;
    background:var(--panel);
    border-radius:30px 34px 0 50px;
    overflow:hidden;
  }
  .plan-panel--management{top:25px}
  .plan-panel--cyber{top:502px}
  .row{display:grid;align-items:center;border-bottom:1px solid var(--line)}
  .plan-panel--management .row{grid-template-columns:464px 125px 125px 170px}
  .plan-panel--cyber .row{grid-template-columns:589px 125px 170px}
  .row > div{height:100%;display:flex;align-items:center;justify-content:center}
  .row > .feature{justify-content:flex-start;padding-left:37px;font-weight:300;font-size:19px;line-height:1.12}
  .row > .value{border-left:1px solid var(--line);font-weight:300;font-size:19px;text-align:center;line-height:1.12}
  .head{background:var(--orange);border-bottom:none}
  .head > .title{font-size:28px;font-weight:600;justify-content:flex-start;padding-left:37px}
  .head > .tier{font-size:24px;font-weight:600}
  .section-band{background:var(--orange);height:45px;display:flex;align-items:center;padding-left:37px;font-size:28px;font-weight:600}
  .price{background:var(--orange);border-bottom:1px solid var(--line-light)}
  .price:last-child{border-bottom:none}
  .price > .label{justify-content:flex-end;padding-right:39px;font-weight:700;font-size:16.5px}
  .plan-panel--cyber .price > .label{padding-right:20px}
  .price > .amount{border-left:1px solid var(--line-light);font-weight:700;font-size:17px}
  .mark{width:30px;height:26px}
  .mark--tick{color:var(--tick)}
  .mark--cross{color:var(--cross);width:26px}
</style>
</head>
<body>
<svg width="0" height="0" style="position:absolute" aria-hidden="true">
  <symbol id="tick" viewBox="0 0 30 26"><path d="M2 13 L11 22 L28 3" fill="none" stroke="currentColor" stroke-width="5" stroke-linejoin="miter"/></symbol>
  <symbol id="cross" viewBox="0 0 26 26"><path d="M3 3 L23 23 M23 3 L3 23" fill="none" stroke="currentColor" stroke-width="5"/></symbol>
</svg>

<div class="network-backdrop" role="img" aria-label="Glowing blue technology network of connected nodes"></div>

<section class="plan-panel plan-panel--management">
  <div class="row head" style="height:54px"><div class="title">Management</div><div class="tier">Essential</div><div class="tier">Business</div><div class="tier">Professional</div></div>
  <div class="row" style="height:36px"><div class="feature">Asset and Warranty Tracking &amp;Reporting</div><div class="value"><svg class="mark mark--tick"><use href="#tick"/></svg></div><div class="value"><svg class="mark mark--tick"><use href="#tick"/></svg></div><div class="value"><svg class="mark mark--tick"><use href="#tick"/></svg></div></div>
  <div class="row" style="height:36px"><div class="feature">Comprehensive IT Documentation</div><div class="value"><svg class="mark mark--tick"><use href="#tick"/></svg></div><div class="value"><svg class="mark mark--tick"><use href="#tick"/></svg></div><div class="value"><svg class="mark mark--tick"><use href="#tick"/></svg></div></div>
  <div class="row" style="height:35px"><div class="feature">Technology Strategy Meeting</div><div class="value">Annual</div><div class="value">Quarterly</div><div class="value">Monthly</div></div>
  <div class="row" style="height:40px"><div class="feature">Technology Business Review Meeting</div><div class="value">Annual</div><div class="value">Bi Annual</div><div class="value">Quarterly</div></div>
  <div class="row" style="height:41px;border-bottom:none"><div class="feature">IT Policy Templates</div><div class="value"><svg class="mark mark--cross"><use href="#cross"/></svg></div><div class="value"><svg class="mark mark--tick"><use href="#tick"/></svg></div><div class="value"><svg class="mark mark--tick"><use href="#tick"/></svg></div></div>
  <div class="section-band">Training</div>
  <div class="row" style="height:44px"><div class="feature">End User Training Materials</div><div class="value"><svg class="mark mark--cross"><use href="#cross"/></svg></div><div class="value"><svg class="mark mark--cross"><use href="#cross"/></svg></div><div class="value"><svg class="mark mark--tick"><use href="#tick"/></svg></div></div>
  <div class="row" style="height:45px;border-bottom:none"><div class="feature">Security Awareness Training</div><div class="value"><svg class="mark mark--tick"><use href="#tick"/></svg></div><div class="value"><svg class="mark mark--tick"><use href="#tick"/></svg></div><div class="value"><svg class="mark mark--tick"><use href="#tick"/></svg></div></div>
  <div class="row price" style="height:33px"><div class="label">RRP / User</div><div class="amount">$110</div><div class="amount">$130</div><div class="amount">$165</div></div>
  <div class="row price" style="height:25px"><div class="label">Minimum User Count</div><div class="amount">5</div><div class="amount">5</div><div class="amount">5</div></div>
  <div class="row price" style="height:27px"><div class="label">Minimum Monthly Commit</div><div class="amount">$550</div><div class="amount">$650</div><div class="amount">$825</div></div>
</section>

<section class="plan-panel plan-panel--cyber">
  <div class="row head" style="height:54px"><div class="title">Cybersecurity Packages</div><div class="tier">Business</div><div class="tier">Professional</div></div>
  <div class="row" style="height:32px"><div class="feature">Compliance with NCSB Essential 8 Maturity</div><div class="value">Level 0</div><div class="value">Level 1</div></div>
  <div class="row" style="height:64px"><div class="feature">Security Standard - Alignment to Helpdesk<br>CS365 Security Policy &amp; Reporting</div><div class="value"><svg class="mark mark--tick"><use href="#tick"/></svg></div><div class="value"><svg class="mark mark--tick"><use href="#tick"/></svg></div></div>
  <div class="row" style="height:57px"><div class="feature">24x7 Security Operations Centre (SOC) -<br>Monitoring CloudOffice</div><div class="value"><svg class="mark mark--tick"><use href="#tick"/></svg></div><div class="value"><svg class="mark mark--tick"><use href="#tick"/></svg></div></div>
  <div class="row" style="height:32px"><div class="feature">Dark Web Scanning</div><div class="value"><svg class="mark mark--tick"><use href="#tick"/></svg></div><div class="value"><svg class="mark mark--tick"><use href="#tick"/></svg></div></div>
  <div class="row" style="height:34px"><div class="feature">Cloud Email Filtering</div><div class="value"><svg class="mark mark--tick"><use href="#tick"/></svg></div><div class="value"><svg class="mark mark--tick"><use href="#tick"/></svg></div></div>
  <div class="row" style="height:33px"><div class="feature">CloudSuite Backup</div><div class="value"><svg class="mark mark--tick"><use href="#tick"/></svg></div><div class="value"><svg class="mark mark--tick"><use href="#tick"/></svg></div></div>
  <div class="row" style="height:35px"><div class="feature">Automated Email Signatures</div><div class="value"><svg class="mark mark--tick"><use href="#tick"/></svg></div><div class="value"><svg class="mark mark--tick"><use href="#tick"/></svg></div></div>
  <div class="row" style="height:32px"><div class="feature">Endpoint Protection with EDR - Workstations &amp; Servers</div><div class="value"><svg class="mark mark--tick"><use href="#tick"/></svg></div><div class="value"><svg class="mark mark--tick"><use href="#tick"/></svg></div></div>
  <div class="row" style="height:38px"><div class="feature">3rd Party Applications Updating</div><div class="value"><svg class="mark mark--cross"><use href="#cross"/></svg></div><div class="value"><svg class="mark mark--tick"><use href="#tick"/></svg></div></div>
  <div class="row" style="height:53px"><div class="feature">24x7 Security Operations Centre (SOC) -<br>Monitoring Endpoints and Servers</div><div class="value"><svg class="mark mark--cross"><use href="#cross"/></svg></div><div class="value"><svg class="mark mark--tick"><use href="#tick"/></svg></div></div>
  <div class="row" style="height:33px"><div class="feature">Privileged Access Management &amp; Application Whitelisting</div><div class="value"><svg class="mark mark--cross"><use href="#cross"/></svg></div><div class="value"><svg class="mark mark--tick"><use href="#tick"/></svg></div></div>
  <div class="row" style="height:34px"><div class="feature">Internal Vulnerability Scanning</div><div class="value"><svg class="mark mark--cross"><use href="#cross"/></svg></div><div class="value"><svg class="mark mark--tick"><use href="#tick"/></svg></div></div>
  <div class="row" style="height:62px;border-bottom:none"><div class="feature">Backup &amp; Disaster Recovery to comply with NCSB<br>Essential 8 Maturity Level 1</div><div class="value"><svg class="mark mark--cross"><use href="#cross"/></svg></div><div class="value">Pending<br>Assessment</div></div>
  <div class="row price" style="height:33px"><div class="label">RRP / User</div><div class="amount">$35</div><div class="amount">$60</div></div>
  <div class="row price" style="height:25px"><div class="label">Minimum User Count</div><div class="amount">5</div><div class="amount">5</div></div>
  <div class="row price" style="height:29px"><div class="label">Minimum Monthly Commit</div><div class="amount">$175</div><div class="amount">$300</div></div>
</section>
</body>
</html>
```